MOREVI VEGAN SUSHI

www.morevi-restaurant.de
We are open in 2018 and are an innovative restaurant from Munich. We would like a cool design for our drinks and food menu. It's very simple at the moment. See the File menu. In any case, our logo should appear. On the website we use neutraface as a font. But it's not a must. We are only open in the evening and appeal to a young, upscale audience.

```html
<!DOCTYPE html>
<html lang="de">
<head>
<meta charset="utf-8">
<title>MOREVI – Speisekarte</title>
<link rel="stylesheet" href="https://fonts.googleapis.com/css2?family=Potta+One&family=Raleway:ital,wght@0,300;0,400;0,700;1,400&display=swap">
<style>
  :root {
    --ink: #1a1a1a;
    --gold: #c9a048;
    --blue: #0e6f9c;
    --beige: #f1dccb;
    --mist: #dbe9f4;
    --paper: #ffffff;
    --canvas: #ffffff;
  }
  * { box-sizing: border-box; margin: 0; padding: 0; }
  html, body { width: 1200px; height: 815px; overflow: hidden; background: var(--canvas); }
  body { position: relative; font-family: "Raleway", sans-serif; color: var(--ink); }

  .menu-page {
    position: absolute; width: 546px; height: 772px;
    background: var(--paper); outline: 1px solid #bdbdbd; overflow: hidden;
  }
  .menu-page--food-sets { left: 26px; top: 22px; }
  .menu-page--a-la-carte { left: 624px; top: 25px; }
  .page-backdrop { position: absolute; inset: 0; width: 546px; height: 772px; }

  .brand-mark { position: absolute; left: 0; width: 546px; text-align: center; }
  .brand-mark__dot { position: absolute; left: 251px; top: 62px; width: 44px; height: 44px; border-radius: 50%; background: var(--ink); }
  .brand-mark__name {
    position: absolute; left: 0; top: 131px; width: 546px; text-align: center;
    font-weight: 300; font-size: 15px; letter-spacing: 12px; padding-left: 12px;
  }

  .block { position: absolute; text-align: center; font-size: 11.5px; line-height: 14.6px; }
  .block--center { left: 0; width: 546px; }
  .section-title {
    font-family: "Potta One", sans-serif; color: var(--gold);
    font-size: 17px; line-height: 20px; letter-spacing: 0.5px; font-weight: 400;
  }
  .price { font-size: 15.5px; line-height: 20px; margin-top: 2px; }
  .block em { font-style: italic; }
  .block b { font-weight: 700; }

  .set { width: 170px; }
  .set--1 { left: 11px; top: 426px; }
  .set--2 { left: 184px; top: 426px; }
  .set--3 { left: 358px; top: 426px; }
  .set .section-title { margin-bottom: 2px; }

  .column { position: absolute; text-align: left; font-size: 11.5px; line-height: 14.65px; }
  .column--sushi { left: 44px; top: 271px; }
  .column--small { left: 281px; top: 271px; }

  .main-dish + .main-dish { margin-top: 6px; }

  .footer-note { position: absolute; left: 25px; top: 730px; color: var(--paper); }
  .footer-note__title { font-weight: 700; font-size: 12px; line-height: 14px; }
  .footer-note__text { font-size: 8px; line-height: 10.5px; margin-top: 4px; }
</style>
</head>
<body>

<section class="menu-page menu-page--food-sets">
  <svg class="page-backdrop" viewBox="0 0 546 772" aria-hidden="false">
    <polygon points="0,0 199,0 0,99" fill="var(--blue)" role="img" aria-label="Blaues Wellenmuster"/>
    <polygon points="160,0 546,0 546,59 424,110" fill="var(--gold)"/>
    <polygon points="424,110 546,59 546,160" fill="var(--beige)" role="img" aria-label="Beiges Asanoha-Muster"/>
    <circle cx="28" cy="176" r="39" fill="var(--beige)" role="img" aria-label="Runde beige Musterfläche"/>
    <circle cx="512" cy="529" r="70" fill="var(--mist)" role="img" aria-label="Hellblaues Wellenmuster, rund"/>
    <polygon points="0,609 119,659 0,708" fill="var(--beige)" role="img" aria-label="Beiges Asanoha-Muster"/>
    <polygon points="0,708 119,658 393,772 0,772" fill="var(--gold)"/>
    <polygon points="344,772 546,667 546,772" fill="var(--blue)" role="img" aria-label="Blaues Wellenmuster"/>
  </svg>

  <div class="brand-mark">
    <span class="brand-mark__dot"></span>
    <div class="brand-mark__name">MOREVI</div>
  </div>

  <div class="block block--center" style="top:180px">
    <h2 class="section-title">CHEF MENÜ MIT APERITIV</h2>
    <p><em>für 2 Personen</em></p>
    <p>Kleine Portion RAMENSUPPE <em>mit Gemüse &amp; Nudeln</em></p>
    <p>MINI SET</p>
    <p>DESSERT</p>
    <p class="price">81,00€</p>
  </div>

  <div class="block block--center" style="top:294px">
    <h2 class="section-title">OMAKASE</h2>
    <p><em>für 2 Personen</em></p>
    <p style="line-height:13.4px">EDAMAME</p>
    <p style="line-height:13.4px">OMAKASE SET <em>mit 8 Spezialitäten des Hauses</em></p>
    <p style="line-height:13.4px">PANA COTTA <em>mit Beeren</em></p>
    <p class="price">68,00€</p>
  </div>

  <div class="block set set--1">
    <h2 class="section-title">SET 1</h2>
    <p>HOSOMAKI</p><p>FUTOMAKI</p><p>NIGIRI</p><p>KÜRBISKROKETTEN</p>
    <p>WAKAME GURKEN SALAT</p><p>PICKLES</p><p>GYOZA TEIGTASCHEN</p><p>SUSHI CAKE</p>
    <p class="price">33,90€</p>
  </div>
  <div class="block set set--2">
    <h2 class="section-title">SET 2</h2>
    <p>HOSOMAKI</p><p>FUTOMAKI</p><p>PICKLES</p><p>SUSHI “THUNA” CAKE</p>
    <p>Crispy AUBERGINEN <em>mit Mayo</em></p><p>AUBERGINE DENGAKU</p>
    <p class="price">31,90€</p>
  </div>
  <div class="block set set--3">
    <h2 class="section-title">SET 3</h2>
    <p>HOSOMAKI</p><p>URAMAKI</p><p>NIGIRI</p><p>GEMÜSE TEMPURA</p>
    <p>Crispy TOFUSTICKS <em>mit Mayo</em></p><p>WAKAME SHIRA AE</p>
    <p class="price">28,90€</p>
  </div>

  <div class="footer-note">
    <p class="footer-note__title">All Vegan</p>
    <p class="footer-note__text">Bitte teilen Sie dem Service unbedingt Allergien mit und<br>fragen Sie nach&nbsp; der Allergiker-Menükarte</p>
  </div>
</section>

<section class="menu-page menu-page--a-la-carte">
  <svg class="page-backdrop" viewBox="0 0 546 772">
    <polygon points="0,0 199,0 0,99" fill="var(--blue)" role="img" aria-label="Blaues Wellenmuster"/>
    <polygon points="160,0 546,0 546,59 424,110" fill="var(--gold)"/>
    <polygon points="424,110 546,59 546,160" fill="var(--beige)" role="img" aria-label="Beiges Asanoha-Muster"/>
    <circle cx="28" cy="176" r="39" fill="var(--beige)" role="img" aria-label="Runde beige Musterfläche"/>
    <circle cx="512" cy="529" r="70" fill="var(--mist)" role="img" aria-label="Hellblaues Wellenmuster, rund"/>
    <polygon points="0,609 119,659 0,708" fill="var(--beige)" role="img" aria-label="Beiges Asanoha-Muster"/>
    <polygon points="0,708 119,658 393,772 0,772" fill="var(--gold)"/>
    <polygon points="344,772 546,667 546,772" fill="var(--blue)" role="img" aria-label="Blaues Wellenmuster"/>
  </svg>

  <div class="brand-mark">
    <span class="brand-mark__dot"></span>
    <div class="brand-mark__name">MOREVI</div>
  </div>

  <div class="block block--center" style="top:169px">
    <h2 class="section-title">VORSPEISEN</h2>
    <p>MISO SUPPE <b>5,50€</b></p>
    <p>EDAMAME MIT SALZ/CHILI <b>4,50€</b></p>
    <p>SEIDENTOFU in hausgemachter Sauce mit Mandeln <b>5,50€</b></p>
  </div>

  <div class="column column--sushi">
    <h2 class="section-title">SUSHI</h2>
    <p>URAMAKI mit Tempuragemüse <b>8,90€</b></p>
    <p>FUTOMAKI wechselndes Gemüse <b>8,00€</b></p>
    <p>URAMAKI mit Austernpilze <b>7,50€</b></p>
    <p>HOSOMAKI Gurke Avocado <b>5,50€</b></p>
    <p>HOSOMAKI Gurke Shiitake <b>5,50€</b></p>
    <p>TOMATEN NIGIRI <b>4,50€</b></p>
  </div>
  <div class="column column--small">
    <h2 class="section-title">KLEINE GERICHTE</h2>
    <p>GEMÜSE TEMPURA <b>8,00€</b></p>
    <p>Crispy TOFUSTICKS mit Mayo <b>8,00€</b></p>
    <p>KÜRBISKROKETTEN mit TANGASHU <b>7,90€</b></p>
    <p>SUSHI “THUNA” CAKE <b>6,90€</b></p>
    <p>SUSHI CAKE CLASSIC <b>6,00€</b></p>
    <p>AUBERGINE DENGAKU <b>5,50€</b></p>
  </div>

  <div class="block block--center" style="top:382px">
    <h2 class="section-title">HAUPTSPEISEN</h2>
    <div class="main-dish"><p>Herrlich cremiges KATSU CURRY mit knusprigen Auberginensticks, Reis &amp; Pickles</p><p class="price">17,90€</p></div>
    <div class="main-dish"><p>RAMEN SUPPE mit Nudeln, Gemüse &amp; Tofu</p><p class="price">14,90€</p></div>
    <div class="main-dish"><p>CHIRASHI SUSHI BOWL</p><p class="price">13,90€</p></div>
    <div class="main-dish"><p>SOMMERSALATE mit Sesamdressing &amp; crispy Tofusticks mit Mayo</p><p class="price">12,50€</p></div>
  </div>

  <div class="block block--center" style="top:587px">
    <h2 class="section-title">DESSERT</h2>
    <p>CHEESECAKE mit Beeren <b>6,50€</b></p>
    <p>PANA COTTA mit Beeren <b>5,90€</b></p>
    <p>SORBET des Tages <b>5,50€</b></p>
    <p>SORBET des Tages mit Schuss <b>6,90€</b></p>
  </div>

  <div class="footer-note">
    <p class="footer-note__title">All Vegan</p>
    <p class="footer-note__text">Bitte teilen Sie dem Service unbedingt Allergien mit und<br>fragen Sie nach&nbsp; der Allergiker-Menükarte</p>
  </div>
</section>

</body>
</html>
```